Swimming Pool Service Website needed!!!

Hi Everyone! Thanks for looking at my contest. I PROMISE to provide excellent feedback during this process.

I am starting a new swimming pool business cleaning company in San Diego, California and would like your help in making it similar to one of these two websites that are already functioning.

http://www.brightlagoonworks.example/services-repair.html

http://tidemarkaquacare.example/commercial-pool-cleaning.php

I like these two because they are easy to read, classy, sophisticated and have nice pictures of really clean & clear pools.

I really like the blue on white color format.

I do not have a logo, but the name of my company is GLIMMERWAVE POOL SERVICE.

My tag line is: Water so pure, it sparkles like a summer sky. (does not need to have the quotes around "in"...maybe just italics for this word IN?) You decide for me.

I would like to have a logo designed that incorporates some sort of easy to read letters. I do not want cursive (handwriting) letters. I thought about having a "reflection" of letters (mirror image), but think that this will be hard to read from far away. Maybe you can surprise me and come up with an idea that works using the a mirror image....but I'm not sure. I was leaning toward plain old BLOCK letters as I think it would be easy to read on my truck.

I would like to have 5 pages on my website:
1) Home
2) About Us (Know Your Poolman) / Why Hire Us
3) Services Offered
4) FAQ's
5) Contact

I am looking for a fully-functioning website (coded). Upon selection of the design winner, I am offering to increase the budget/payment by $100-$125 for the coding of all the pages. So anyone looking at participating in this contest, should be willing and able to provide the coding to the webpages that i've requested.

Target Market(s)

Upper middle-class homeowners who have a pool

Industry/Entity Type

Pool Service

Number of Pages Required

5+ page

Font styles to use
Serif

Colors
0455a3
3276b5
85acd3
85cae6
ffffff
33a6d7
0592cd

Requirements
Must have
• The Home page must have this picture highlighted in the top of the page:
• http://www.mesawaterpro.example/
• Must have pictures of some high-end pools. Any that you can find on the internet are wonderful.
• Must have a table on the right of the home page that mentions the service areas that we go to:
• • Carmel Valley (92130)
• • Del Mar (92014)
• • Rancho Santa Fe (92067)
• • Solana Beach (92075)
• • Santaluz (92127)
• • Cardiff (92007)
• • Encinitas (92024)
• • Carlsbad (92009, 92008)
• • La Jolla (92037)
• • Pacific Beach (92109)
• • Mira Mesa (92126)
• • Sorrento Valley (92121)
• • Clairemont (92117)
• • Rancho Bernardo (92127, 92128)
• • Rancho Penasquitos (92129)
• • Poway (92064)
• •
Nice to have
• Maybe incorporate some pictures of some kids (or families) playing in pools on the Why Hire Us page?
• I also like the feel of this website, but posting this page just for reference so you can get a feel more of what I like:
• http://www.crestlinepool.example/
• I like the FAQ's page from this website. I like how you can click on the question and then it pops up with the answer. http://www.dunewoodpoolcare.example/pool-spa-fountain-faqs/

```html
<!DOCTYPE html>
<html lang="en">
<head>
<meta charset="utf-8">
<title>Glimmerwave Pool Service</title>
<link href="https://fonts.googleapis.com/css2?family=Raleway:wght@300;400;500;600&family=Open+Sans:ital,wght@0,400;0,600;0,700;1,400&display=swap" rel="stylesheet">
<style>
:root{
  --navy:#0455a3;
  --blue:#3276b5;
  --sky:#33a6d7;
  --ocean:#0592cd;
  --pale:#85cae6;
  --mist:#85acd3;
  --white:#ffffff;
  --text:#3a3a3a;
  --line:#9cc6e4;
  --dark:#161616;
}
*{box-sizing:border-box;margin:0;padding:0}
html,body{width:1200px;height:4358px;overflow:hidden}
body{font-family:"Open Sans",Arial,sans-serif;color:var(--text);background:var(--white);position:relative}

/* header */
.site-header{position:absolute;left:0;top:0;width:1200px;height:84px;background:var(--white)}
.brand{position:absolute;left:92px;top:12px;font-family:"Raleway",Arial,sans-serif;font-weight:500;color:var(--ocean);line-height:1}
.brand .name{font-size:40px;display:block}
.brand .sub{font-size:15px;letter-spacing:4px;display:block;margin-top:3px}
.main-nav{position:absolute;right:92px;top:32px;display:flex;gap:40px;font-family:"Raleway",Arial,sans-serif;font-size:13px;letter-spacing:1px;color:#555}

/* hero */
.hero{position:absolute;left:0;top:84px;width:1200px;height:492px;background:linear-gradient(180deg,#bfe3f5 0%,#a5d6ef 45%,#c9e7f6 100%)}
.hero-band{position:absolute;left:0;top:0;width:1200px;height:34px;background:linear-gradient(180deg,#4fa9dc 0%,#8ccbec 100%)}
.hero-photo{position:absolute;left:141px;top:76px;width:918px;height:343px;border:8px solid var(--white);
  background:radial-gradient(ellipse at 25% 25%,#f2fafd 0%,rgba(242,250,253,0) 45%),
             radial-gradient(ellipse at 75% 70%,#1b7cc0 0%,rgba(27,124,192,0) 60%),
             linear-gradient(150deg,#d8eef8 0%,#7cc6e9 35%,#3aa4d8 65%,#1f86c6 100%)}
.tagline{position:absolute;left:0;top:426px;width:1200px;text-align:center;font-size:20px;font-weight:600;color:var(--white)}
.tagline em{font-style:italic}
.dots{display:flex;gap:10px;justify-content:center}
.dot{width:11px;height:11px;border-radius:50%;background:rgba(255,255,255,.55)}
.dot.on{background:var(--white)}
.hero .dots{position:absolute;left:0;width:1200px;top:466px}

/* intro */
.intro-title{position:absolute;left:100px;top:634px;width:1000px;text-align:center;font-family:"Raleway",Arial,sans-serif;font-weight:400;font-size:26px;color:var(--blue);line-height:1.45}
.intro-photo{position:absolute;left:94px;top:730px;width:335px;height:248px;
  background:radial-gradient(ellipse at 40% 45%,#f3d9c6 0%,rgba(243,217,198,0) 35%),
             linear-gradient(135deg,#cdeefa 0%,#7cc8ea 50%,#3fa3d9 100%)}
.intro-copy{position:absolute;left:613px;top:738px;width:493px;font-size:14px;line-height:22px;color:var(--text)}
.intro-copy p{margin-bottom:14px}
.intro-copy a{color:var(--ocean);text-decoration:none}

/* projects */
.projects{position:absolute;left:0;top:1042px;width:1200px;height:878px;background:linear-gradient(180deg,#7fc0e6 0%,#5fb0df 50%,#7cc1e7 100%)}
.section-title{font-family:"Raleway",Arial,sans-serif;font-weight:400;text-align:center}
.projects .section-title{position:absolute;left:0;top:38px;width:1200px;font-size:38px;color:var(--white)}
.project-grid{position:absolute;left:94px;top:120px;width:1012px;display:grid;grid-template-columns:repeat(3,1fr)}
.project{height:337px}
.p1{background:radial-gradient(ellipse at 50% 80%,#39a9de 0%,rgba(57,169,222,0) 55%),linear-gradient(180deg,#7d8a5c 0%,#a7a98a 35%,#4f9fc6 65%,#1f8fcf 100%)}
.p2{background:radial-gradient(ellipse at 50% 80%,#6fd0df 0%,rgba(111,208,223,0) 55%),linear-gradient(180deg,#4b4a7c 0%,#9c80a2 40%,#c49a8c 60%,#4eb3cc 100%)}
.p3{background:radial-gradient(ellipse at 45% 85%,#3ab0d2 0%,rgba(58,176,210,0) 55%),linear-gradient(180deg,#d4dde2 0%,#9aa7ad 35%,#7d6a5a 60%,#3d9fc1 100%)}
.p4{background:radial-gradient(ellipse at 60% 80%,#1e9bd8 0%,rgba(30,155,216,0) 55%),linear-gradient(180deg,#8fc3e9 0%,#f2f5f7 40%,#9fd6ef 60%,#2fa2d9 100%)}
.p5{background:radial-gradient(ellipse at 50% 85%,#73dbe5 0%,rgba(115,219,229,0) 55%),linear-gradient(180deg,#172234 0%,#3c4d5f 40%,#8c7a4f 58%,#4fbfd6 100%)}
.p6{background:radial-gradient(ellipse at 50% 80%,#5fc4de 0%,rgba(95,196,222,0) 55%),linear-gradient(180deg,#8e6a48 0%,#c9a884 40%,#d7c1a2 55%,#49aed1 100%)}

/* services */
.services-title{position:absolute;left:94px;top:1962px;width:640px;font-size:38px;color:var(--ocean)}
.areas-title{position:absolute;left:787px;top:1962px;font-size:38px;color:var(--ocean);text-align:left}
.service-list{position:absolute;list-style:none}
.service-list li{position:absolute;left:0;width:300px;font-size:17px;line-height:27px;color:var(--navy);padding-left:50px}
.service-list li svg{position:absolute;left:0;top:4px}
.col-a{left:94px;top:2058px}
.col-b{left:446px;top:2058px}
.area-list{position:absolute;left:787px;top:2057px;width:319px;list-style:none}
.area-list li{height:40px;margin-bottom:12px;border:1px solid var(--line);font-size:15px;color:var(--blue);padding:9px 10px}

/* testimonials */
.testimonials{position:absolute;left:0;top:3139px;width:1200px;height:389px;background:linear-gradient(180deg,#86c7e9 0%,#64b3df 100%)}
.testimonials .section-title{position:absolute;left:0;top:40px;width:1200px;font-size:38px;color:var(--white)}
.quote{position:absolute;left:150px;top:136px;width:900px;text-align:center;font-size:17px;font-style:italic;line-height:1.7;color:var(--white)}
.quote strong{font-weight:700}
.quote-name{position:absolute;left:0;top:246px;width:1200px;text-align:center;font-size:13px;letter-spacing:1px;color:var(--white)}
.testimonials .dots{position:absolute;left:0;width:1200px;top:295px}

/* contact */
.contact-copy{position:absolute;left:94px;top:3616px;width:460px;font-size:14px;line-height:22px}
.contact-copy p{margin-bottom:14px}
.contact-copy a{color:var(--ocean);text-decoration:none}
.contact-form{position:absolute;left:613px;top:3612px;width:493px}
.field{height:42px;border:1px solid var(--line);margin-bottom:15px;font-size:14px;color:var(--mist);padding:11px 14px}
.field.message{height:228px}
.send{margin-top:16px;width:82px;height:46px;border:1px solid var(--line);color:var(--ocean);font-size:13px;letter-spacing:1px;text-align:center;line-height:44px}

/* footer */
.site-footer{position:absolute;left:0;top:4174px;width:1200px;height:184px;background:var(--dark)}
.to-top{position:absolute;left:588px;top:36px}
.copyright{position:absolute;left:94px;top:140px;font-size:12px;color:#cfcfcf}
</style>
</head>
<body>

<header class="site-header">
  <div class="brand"><span class="name">Glimmerwave</span><span class="sub">POOL SERVICE</span></div>
  <nav class="main-nav">
    <span>HOME</span><span>ABOUT US</span><span>SERVICES OFFERED</span><span>FAQ'S</span><span>WHY HIRE US</span><span>CONTACT</span>
  </nav>
</header>

<section class="hero">
  <div class="hero-band"></div>
  <div class="hero-photo" role="img" aria-label="Clear blue swimming pool with chrome ladder steps"></div>
  <p class="tagline">Water so pure, it sparkles like a <em>summer sky</em>.</p>
  <div class="dots"><span class="dot"></span><span class="dot on"></span></div>
</section>

<h2 class="intro-title">Glimmerwave Pool Service is a leading San Diego swimming pool &amp; spa service company for both residential pools and commercial pools</h2>
<div class="intro-photo" role="img" aria-label="Child in goggles swimming in a pool"></div>
<div class="intro-copy">
  <p>If you're looking for the BEST pool cleaning service at an affordable price available in San Diego, we would love the opportunity to prove that Glimmerwave Pool Service is the answer. We are a family-owned company that was built on integrity and a commitment to earn and keep each customer's trust with every service and repair.</p>
  <p>Customer satisfaction is our highest priority, and we are proud to see how many of our wonderful customers leave great <a>reviews</a>.</p>
</div>

<section class="projects">
  <h2 class="section-title">Recent Projects</h2>
  <div class="project-grid">
    <div class="project p1" role="img" aria-label="Resort pool framed by palm trees"></div>
    <div class="project p2" role="img" aria-label="Backyard pool at dusk"></div>
    <div class="project p3" role="img" aria-label="Indoor pool under a glass roof"></div>
    <div class="project p4" role="img" aria-label="Infinity pool overlooking the ocean"></div>
    <div class="project p5" role="img" aria-label="Lit pool and waterfall at night"></div>
    <div class="project p6" role="img" aria-label="Indoor lap pool with tiled surround"></div>
  </div>
</section>

<h2 class="section-title services-title">Our Services</h2>
<h2 class="section-title areas-title">Service Areas</h2>

<ul class="service-list col-a">
  <li style="top:0"><svg width="26" height="22" viewBox="0 0 26 22"><path d="M2 12 L9 19 L24 2" fill="none" stroke="#0592cd" stroke-width="4"/></svg>Swimming Pool and Spa Cleaning</li>
  <li style="top:104px"><svg width="26" height="22" viewBox="0 0 26 22"><path d="M2 12 L9 19 L24 2" fill="none" stroke="#0592cd" stroke-width="4"/></svg>New Pool and Spa Start Ups</li>
  <li style="top:188px"><svg width="26" height="22" viewBox="0 0 26 22"><path d="M2 12 L9 19 L24 2" fill="none" stroke="#0592cd" stroke-width="4"/></svg>Troubleshoot and Repair pumps, filters, heaters and heat exchangers</li>
  <li style="top:318px"><svg width="26" height="22" viewBox="0 0 26 22"><path d="M2 12 L9 19 L24 2" fill="none" stroke="#0592cd" stroke-width="4"/></svg>Tile Cleaning &amp; Restoration</li>
  <li style="top:402px"><svg width="26" height="22" viewBox="0 0 26 22"><path d="M2 12 L9 19 L24 2" fill="none" stroke="#0592cd" stroke-width="4"/></svg>CPO (Certified Pool Operator) Insured</li>
  <li style="top:509px"><svg width="26" height="22" viewBox="0 0 26 22"><path d="M2 12 L9 19 L24 2" fill="none" stroke="#0592cd" stroke-width="4"/></svg>Reliable and affordable pool and spa maintenance</li>
  <li style="top:613px"><svg width="26" height="22" viewBox="0 0 26 22"><path d="M2 12 L9 19 L24 2" fill="none" stroke="#0592cd" stroke-width="4"/></svg>Brushing walls and tile cleaning</li>
  <li style="top:720px"><svg width="26" height="22" viewBox="0 0 26 22"><path d="M2 12 L9 19 L24 2" fill="none" stroke="#0592cd" stroke-width="4"/></svg>Pool leakage detection and repairs</li>
  <li style="top:824px"><svg width="26" height="22" viewBox="0 0 26 22"><path d="M2 12 L9 19 L24 2" fill="none" stroke="#0592cd" stroke-width="4"/></svg>Eliminating leaves and debris</li>
  <li style="top:904px"><svg width="26" height="22" viewBox="0 0 26 22"><path d="M2 12 L9 19 L24 2" fill="none" stroke="#0592cd" stroke-width="4"/></svg>Prompt swimming pool cleaning each week</li>
</ul>

<ul class="service-list col-b">
  <li style="top:0"><svg width="26" height="22" viewBox="0 0 26 22"><path d="M2 12 L9 19 L24 2" fill="none" stroke="#0592cd" stroke-width="4"/></svg>Install and repair lighting</li>
  <li style="top:80px"><svg width="26" height="22" viewBox="0 0 26 22"><path d="M2 12 L9 19 L24 2" fill="none" stroke="#0592cd" stroke-width="4"/></svg>Leak Detection Salt System Conversions</li>
  <li style="top:188px"><svg width="26" height="22" viewBox="0 0 26 22"><path d="M2 12 L9 19 L24 2" fill="none" stroke="#0592cd" stroke-width="4"/></svg>Fountain Cleaning and Service</li>
  <li style="top:295px"><svg width="26" height="22" viewBox="0 0 26 22"><path d="M2 12 L9 19 L24 2" fill="none" stroke="#0592cd" stroke-width="4"/></svg>Licensed and Bonded Swimming Pool Technicians</li>
  <li style="top:402px"><svg width="26" height="22" viewBox="0 0 26 22"><path d="M2 12 L9 19 L24 2" fill="none" stroke="#0592cd" stroke-width="4"/></svg>Low Rates for Repairs, Maintenance, Cleaning</li>
  <li style="top:509px"><svg width="26" height="22" viewBox="0 0 26 22"><path d="M2 12 L9 19 L24 2" fill="none" stroke="#0592cd" stroke-width="4"/></svg>Friendly assistance from the staff</li>
  <li style="top:613px"><svg width="26" height="22" viewBox="0 0 26 22"><path d="M2 12 L9 19 L24 2" fill="none" stroke="#0592cd" stroke-width="4"/></svg>Salt water system maintenance</li>
  <li style="top:720px"><svg width="26" height="22" viewBox="0 0 26 22"><path d="M2 12 L9 19 L24 2" fill="none" stroke="#0592cd" stroke-width="4"/></svg>Making your pool and spa crystal clear with balanced chemicals</li>
  <li style="top:851px"><svg width="26" height="22" viewBox="0 0 26 22"><path d="M2 12 L9 19 L24 2" fill="none" stroke="#0592cd" stroke-width="4"/></svg>Noisy pool motor repairs</li>
  <li style="top:931px"><svg width="26" height="22" viewBox="0 0 26 22"><path d="M2 12 L9 19 L24 2" fill="none" stroke="#0592cd" stroke-width="4"/></svg>Cleaning out debris in skimmer and pool pump basket</li>
</ul>

<ul class="area-list">
  <li>Carmel Valley (92130)</li>
  <li>Del Mar (92014)</li>
  <li>Rancho Santa Fe (92067)</li>
  <li>Solana Beach (92075)</li>
  <li>Santaluz (92127)</li>
  <li>Cardiff (92007)</li>
  <li>Encinitas (92024)</li>
  <li>Carlsbad (92009, 92008)</li>
  <li>La Jolla (92037)</li>
  <li>Pacific Beach (92109)</li>
  <li>Mira Mesa (92126)</li>
  <li>Sorrento Valley (92121)</li>
  <li>Clairemont (92117)</li>
  <li>Rancho Bernardo (92127, 92128)</li>
  <li>Rancho Penasquitos (92129)</li>
  <li>Poway (92064)</li>
</ul>

<section class="testimonials">
  <h2 class="section-title">What Our Clients Say</h2>
  <p class="quote">"Working with Dale is <strong>terrific</strong>. His education and professional background sets him apart from all the other pool cleaners. He has excellent communication with us and he shows up when he says he will. Glimmerwave is the only pool care company I have ever recommended to my friends."</p>
  <p class="quote-name">MARTIN KESSLER</p>
  <div class="dots"><span class="dot on"></span><span class="dot"></span></div>
</section>

<div class="contact-copy">
  <p>We <strong>guarantee your satisfaction</strong> on each and every service call and repair. Your pool, spa or fountain should be a blessing and not a hassle or a headache. Trust Glimmerwave Pool Service to keep your water sparkling and clear and your equipment in top-notch shape!</p>
  <p>If it's got a pump and a filter we can clean it, repair it, and keep it in top condition! Give us a call at (555) 014-2287, fill out the form to the right, or go to our <a>Contact Us</a> page now.</p>
</div>

<form class="contact-form">
  <div class="field">Your Name</div>
  <div class="field">Your Email</div>
  <div class="field">Your Phone Number</div>
  <div class="field message">Your Message</div>
  <div class="send">SEND</div>
</form>

<footer class="site-footer">
  <svg class="to-top" width="24" height="16" viewBox="0 0 24 16" aria-label="Back to top"><path d="M2 14 L12 4 L22 14" fill="none" stroke="#ffffff" stroke-width="3"/></svg>
  <p class="copyright">Copyright © 2015 Glimmerwave Pool Service</p>
</footer>

</body>
</html>
```